Great looking banner designs for our website www.stoutwellcases.com

Our website is a key marketing platform and the banners need some work. We need 4-5 great looking banner designs.
StoutWell cases are the toughest around and have a unique accessory attachment system and range of accessories. We like to see banners that show our products, how they can be used and with key selling messages

Target Market(s)

Key markets are construction and outdoor workers, fishing and boating, cycling, camping and other adventure activities.

Industry/Entity Type

Marketing

Font styles to use
Other font styles liked:
• Homenaje

Requirements
Must have
• Ideally we'd like the banners to give customers a good idea of the capabilities of our products and the situations they can be used.

This is a dropbox link to a range of images and renders that can be used for the banners.
https://www.parcelnest.com/sh/k7p2qx9ma3tz118/Tq4vLmw8nE

We are also happy to look at increasing the banner size on the home page.

Banners should show the Zelvar case range + different accessories.
We have our new Stoutwell outdoor Bluetooth speaker arriving soon so need an appropriate banner
Banner size should be 1270 x 520

```html
<!DOCTYPE html>
<html lang="en">
<head>
<meta charset="utf-8">
<title>StoutWell Cases – Feel Free to Be Bold</title>
<link rel="stylesheet" href="https://fonts.googleapis.com/css2?family=Homenaje&family=Oswald:wght@500;600&display=swap">
<style>
  :root {
    --brand-orange: #e8731c;
    --case-orange: #f47a1e;
    --case-orange-deep: #c85a10;
    --case-grey: #a9a9a6;
    --case-grey-deep: #7d7d7a;
    --text-white: #ffffff;
    --scene-dark: #26221e;
    --scene-mid: #4e4842;
    --scene-light: #c9c8c5;
    --scene-warm: #6e4a22;
  }
  * { margin: 0; padding: 0; box-sizing: border-box; }
  html, body {
    width: 1200px;
    height: 491px;
    overflow: hidden;
    background: var(--scene-dark);
  }
  .banner {
    position: relative;
    width: 1200px;
    height: 491px;
    overflow: hidden;
  }
  .hero-photo {
    position: absolute;
    inset: 0;
    background:
      radial-gradient(ellipse 300px 260px at 1050px 150px, rgba(235,235,232,0.85), transparent 72%),
      radial-gradient(ellipse 420px 160px at 880px 470px, rgba(120,80,30,0.6), transparent 70%),
      radial-gradient(ellipse 200px 260px at 60px 120px, rgba(120,80,36,0.7), transparent 70%),
      linear-gradient(110deg, var(--scene-warm) 0%, var(--scene-dark) 25%, var(--scene-mid) 55%, var(--scene-light) 100%);
  }
  .photo-zone {
    position: absolute;
    border-radius: 34px;
  }
  .photo-zone--grey-case {
    left: 470px;
    top: -40px;
    width: 380px;
    height: 260px;
    transform: rotate(28deg);
    background: linear-gradient(160deg, var(--case-grey) 0%, var(--case-grey-deep) 100%);
    opacity: 0.9;
  }
  .photo-zone--orange-case {
    left: 240px;
    top: 20px;
    width: 330px;
    height: 500px;
    transform: rotate(9deg);
    background: linear-gradient(150deg, var(--case-orange) 0%, var(--case-orange-deep) 100%);
  }
  .photo-zone--screen {
    left: 285px;
    top: 85px;
    width: 240px;
    height: 340px;
    border-radius: 10px;
    transform: rotate(9deg);
    background: linear-gradient(170deg, #6a3040 0%, #8d8a92 45%, #c8c6cc 100%);
  }
  .brand {
    position: absolute;
    left: 26px;
    top: 26px;
    display: flex;
    align-items: center;
    gap: 8px;
  }
  .brand-dot {
    width: 22px;
    height: 22px;
    border-radius: 50%;
    background: var(--brand-orange);
  }
  .brand-name {
    font-family: "Oswald", sans-serif;
    font-weight: 500;
    font-size: 22px;
    line-height: 1;
    color: var(--text-white);
  }
  .headline {
    position: absolute;
    left: 593px;
    top: 260px;
    font-weight: normal;
  }
  .headline-lead {
    display: block;
    font-family: "Oswald", sans-serif;
    font-weight: 600;
    font-size: 56px;
    line-height: 1;
    color: var(--text-white);
    transform: scaleX(0.84);
    transform-origin: left center;
  }
  .headline-main {
    display: block;
    margin-left: 100px;
    margin-top: -4px;
    font-family: "Homenaje", sans-serif;
    font-weight: 400;
    font-size: 152px;
    line-height: 1;
    color: var(--brand-orange);
    letter-spacing: -1px;
  }
</style>
</head>
<body>
  <main class="banner">
    <div class="hero-photo" role="img" aria-label="Photo of an orange rugged Zelvar case on wet rocks in a flowing stream, with a grey case beside it and orange wave lines sweeping across">
      <div class="photo-zone photo-zone--grey-case" aria-hidden="true"></div>
      <div class="photo-zone photo-zone--orange-case" aria-hidden="true"></div>
      <div class="photo-zone photo-zone--screen" aria-hidden="true"></div>
    </div>

    <div class="brand">
      <span class="brand-dot"></span>
      <span class="brand-name">StoutWell</span>
    </div>

    <h1 class="headline">
      <span class="headline-lead">FEEL FREE TO</span>
      <span class="headline-main">BE BOLD</span>
    </h1>
  </main>
</body>
</html>
```